Professional business cards for real estate development company

I need business cards for my new real estate development company. The company, "KORVA" is a real estate development, investment, and advisory firm with a focus on multifamily, office, and mixed-use projects across primary and secondary markets in the Southeast United States.

Style preference is modern

Industry/Entity Type

Real Estate Development

Contact Information for Business Card

The business cards need to include:
Name
Title
Mailing Address
Phone Number
Web Address

Logo is attached. I would like white to be the primary color with incorporation of the company colors: #232D3A and #B5A451

Font styles to use
Other font styles liked:
• Montserrat, Avenir

Requirements
Must have
• Company Logo. No need to include the company name since the name is in the logo.
Should not have
• No line type designs

```html
<!DOCTYPE html>
<html lang="en">
<head>
<meta charset="utf-8">
<title>KORVA Business Cards</title>
<link href="https://fonts.googleapis.com/css2?family=Montserrat:wght@500;700;800&family=Lato:wght@400&display=swap" rel="stylesheet">
<style>
  :root {
    --navy: #232d3a;
    --navy-muted: #3a4659;
    --gold: #b5a451;
    --white: #ffffff;
    --backdrop: #d9dadc;
  }
  * { margin: 0; padding: 0; box-sizing: border-box; }
  html, body { width: 1200px; height: 965px; overflow: hidden; }
  body {
    background: var(--backdrop);
    position: relative;
    font-family: "Lato", sans-serif;
  }
  .card {
    position: absolute;
    left: 290px;
    width: 620px;
    height: 354px;
    background: var(--navy);
    box-shadow: 0 6px 18px rgba(0,0,0,0.25);
    overflow: hidden;
  }
  .card--back { top: 98px; }
  .card--front { top: 512px; }

  .back-mark {
    position: absolute;
    inset: 0;
    display: flex;
    align-items: center;
    justify-content: center;
    gap: 18px;
  }
  .back-mark__square {
    width: 30px; height: 30px;
    background: var(--navy-muted);
  }
  .back-mark__name {
    font-family: "Montserrat", sans-serif;
    font-weight: 700;
    font-size: 64px;
    letter-spacing: 4px;
    color: var(--navy-muted);
  }

  .brand {
    position: absolute;
    left: 54px;
    top: 188px;
    display: flex;
    align-items: center;
    gap: 14px;
  }
  .brand__square {
    width: 22px; height: 22px;
    background: var(--white);
  }
  .brand__name {
    font-family: "Montserrat", sans-serif;
    font-weight: 700;
    font-size: 46px;
    letter-spacing: 3px;
    color: var(--white);
  }

  .divider {
    position: absolute;
    left: 306px;
    top: 160px;
    width: 1px;
    height: 118px;
    background: var(--white);
    opacity: 0.8;
  }

  .person {
    position: absolute;
    left: 306px;
    top: 78px;
  }
  .person__name {
    font-family: "Montserrat", sans-serif;
    font-weight: 800;
    font-size: 24px;
    letter-spacing: 0.5px;
    color: var(--white);
    line-height: 1.1;
  }
  .person__title {
    font-family: "Montserrat", sans-serif;
    font-weight: 500;
    font-size: 15px;
    letter-spacing: 1px;
    color: var(--gold);
    margin-top: 2px;
  }

  .contacts {
    position: absolute;
    left: 326px;
    top: 160px;
    list-style: none;
  }
  .contacts__item {
    display: flex;
    align-items: flex-start;
    gap: 10px;
    font-size: 15px;
    line-height: 1.25;
    color: var(--white);
    margin-bottom: 8px;
    white-space: nowrap;
  }
  .contacts__icon {
    width: 16px; height: 16px;
    flex: 0 0 16px;
    margin-top: 1px;
  }
</style>
</head>
<body>
  <section class="card card--back">
    <div class="back-mark">
      <span class="back-mark__square"></span>
      <span class="back-mark__name">KORVA</span>
    </div>
  </section>

  <section class="card card--front">
    <div class="person">
      <div class="person__name">DANA WHITLOCK</div>
      <div class="person__title">PARTNER</div>
    </div>

    <div class="brand">
      <span class="brand__square"></span>
      <span class="brand__name">KORVA</span>
    </div>

    <div class="divider"></div>

    <ul class="contacts">
      <li class="contacts__item">
        <svg class="contacts__icon" viewBox="0 0 16 16" fill="none" stroke="#b5a451" stroke-width="1.4" stroke-linejoin="round">
          <path d="M3 1.5h3l1.2 3.2-1.8 1.2a8 8 0 0 0 4.7 4.7l1.2-1.8 3.2 1.2v3a1.5 1.5 0 0 1-1.6 1.5A13 13 0 0 1 1.5 3.1 1.5 1.5 0 0 1 3 1.5z"/>
        </svg>
        <span>(000) 000-0000</span>
      </li>
      <li class="contacts__item">
        <svg class="contacts__icon" viewBox="0 0 16 16" fill="none" stroke="#b5a451" stroke-width="1.4" stroke-linejoin="round">
          <rect x="1.5" y="3.5" width="13" height="9"/>
          <path d="M1.5 3.5 8 9l6.5-5.5"/>
        </svg>
        <span>info@korvadevelopment.com</span>
      </li>
      <li class="contacts__item">
        <svg class="contacts__icon" viewBox="0 0 16 16" fill="none" stroke="#b5a451" stroke-width="1.3">
          <circle cx="8" cy="8" r="6.5"/>
          <ellipse cx="8" cy="8" rx="3" ry="6.5"/>
          <path d="M1.5 8h13M2.5 4.8h11M2.5 11.2h11"/>
        </svg>
        <span>www.korvadevelopment.com</span>
      </li>
      <li class="contacts__item">
        <svg class="contacts__icon" viewBox="0 0 16 16" fill="none" stroke="#b5a451" stroke-width="1.4" stroke-linejoin="round">
          <path d="M8 15s5-5 5-8.5a5 5 0 0 0-10 0C3 10 8 15 8 15z"/>
          <circle cx="8" cy="6.5" r="1.8"/>
        </svg>
        <span>2240 Alder Crest Way NE<br>Brindle Park, GA 30412</span>
      </li>
    </ul>
  </section>
</body>
</html>
```